Broschüre für Sicherheitsdienstleistungen
Zielgruppe
Sicherheitsunternehmen
Hallo,
Wir möchten gerne eine Broschüre (ca. 12 Seiten) gestalten lassen wo alle unsere verschiedene Dienstleistungen Beschrieben werden und unser unternehmen vorgestellt wird an den Kunden.
Als Hard copy Version von unsere neue Seite : http://kwt.seitenplanung-beispiel.de
Das Design soll Freundlich und Modern Gestaltet werden.
Farbtöne gerne in Weiss und Dunkel Blau
Produktdetails :
Rückendrahtheftung links, 4/4-farbig (beidseitiger Druck, CMYK)
ab 250 g wird der Umschlag zusätzlich genutet
Veredelung Umschlag
beidseitiger UV-Lack glänzend
Format
DIN A4 (21 x 29,7 cm)
Details: Hochformat
Seitenanzahl ca. 10 - 12 (Excl. Umschlag)
Material Umschlag
250g Bilderdruck glänzend
New Website Design :
http://kwt.seitenplanung-beispiel.de

```html
<!DOCTYPE html>
<html lang="de">
<head>
<meta charset="utf-8">
<title>KWT Sicherheitsgruppe – Broschüre</title>
<link rel="stylesheet" href="https://fonts.googleapis.com/css2?family=Roboto+Condensed:wght@300;400;700&family=Roboto:wght@400;700&display=swap">
<style>
:root{
  --bg:#d6d6d6;
  --paper:#ffffff;
  --navy:#2e4a8a;
  --blue:#3d5fa6;
  --blue-soft:rgba(52,84,154,.88);
  --ink:#333b48;
  --sub:#3b5ea8;
}
*{margin:0;padding:0;box-sizing:border-box}
html,body{width:1200px;height:4556px;overflow:hidden}
body{background:var(--bg);position:relative;font-family:"Roboto",sans-serif;color:var(--ink)}
.page{position:absolute;background:var(--paper);overflow:hidden;box-shadow:0 2px 6px rgba(0,0,0,.18)}
.spread-fold{position:absolute;width:1px;background:#cfd3da}
.photo{position:absolute}
.box{position:absolute;background:var(--blue-soft);color:#fff;font-family:"Roboto Condensed",sans-serif}
.box .light{font-weight:300}
.box .bold{font-weight:700}
.col{position:absolute;overflow:hidden;font-size:7.4px;line-height:1.3;text-align:justify}
.col h4{font-family:"Roboto Condensed",sans-serif;font-size:8px;color:var(--sub);font-weight:700;text-transform:uppercase;margin:7px 0 2px;line-height:1.15;text-align:left}
.col h4:first-child{margin-top:0}
.col p{margin-bottom:3px}
.headline{position:absolute;font-family:"Roboto Condensed",sans-serif;color:var(--navy);text-transform:uppercase;line-height:1.05}
.headline b{font-weight:700}
.headline span{font-weight:300}
</style>
</head>
<body>

<!-- Cover -->
<section class="page cover" style="left:376px;top:171px;width:490px;height:690px">
  <div class="photo" role="img" aria-label="Nahaufnahme eines Auges mit digitalem Zielraster in Blautönen" style="left:0;top:0;width:490px;height:465px;background:linear-gradient(100deg,#4a6aa8 0%,#5f7fb8 45%,#8aa3c9 70%,#3f5e96 100%)"></div>
  <div class="box cover-panel" style="left:0;top:0;width:286px;height:597px;background:linear-gradient(180deg,rgba(46,74,138,.55) 0%,rgba(52,84,154,.92) 70%)"></div>
  <div style="position:absolute;left:108px;top:70px;width:80px;height:80px;border-radius:50%;background:#fff"></div>
  <div style="position:absolute;left:108px;top:155px;width:80px;text-align:center;font-family:'Roboto Condensed',sans-serif;font-weight:700;font-size:16px;color:#fff">KWT</div>
  <div style="position:absolute;left:40px;top:222px;width:216px;text-align:center;font-family:'Roboto Condensed',sans-serif;font-size:17px;line-height:1.2;color:#fff">KWT SICHERHEITSGRUPPE<br>HAVEL GMBH</div>
  <div style="position:absolute;left:44px;top:444px;font-family:'Roboto Condensed',sans-serif;color:#fff;font-size:29px;line-height:1.1;text-transform:uppercase">
    <b>Sicherheit</b><br><span style="font-weight:300">und</span> <b>Kompetenz</b><br><span style="font-weight:300">europaweit</span> <b>aus</b><br><b>einer Hand</b>
  </div>
  <div style="position:absolute;left:34px;top:640px;font-family:'Roboto Condensed',sans-serif;font-size:14px;color:var(--blue)">Ihr Sicherheitsdienst bundesweit seit 1999</div>
</section>

<!-- Spread 1: Über uns -->
<section class="page" style="left:110px;top:878px;width:489px;height:688px">
  <div class="photo" role="img" aria-label="Überwachungskamera vor nächtlicher Großstadtskyline" style="left:0;top:0;width:470px;height:688px;background:linear-gradient(180deg,#355a9a 0%,#6f8fbf 40%,#2f4d86 75%,#243c6e 100%)"></div>
  <div class="box" style="left:307px;top:42px;width:106px;height:91px;padding:12px 0 0 14px;font-size:30px;line-height:1"><span class="light">ÜBER</span><br><span class="bold">UNS</span></div>
  <div class="box" style="left:128px;top:550px;width:345px;height:95px;padding:12px 14px;font-size:12.5px;line-height:1.3;text-transform:uppercase">Aufgrund der außergewöhnlichen Organisationsstruktur ist es uns möglich, in äußerstem Maße flexibel und schnell zu agieren. Der Kunde entscheidet über den Umfang und die Schwerpunkte des Einsatzes.</div>
</section>
<section class="page" style="left:599px;top:878px;width:489px;height:688px">
  <div class="col" style="left:28px;top:32px;width:207px;height:100px">
    <p>Viele Unternehmen bieten Ihnen Leistungen, die Sie nicht benötigen – der Service der KWT Nord ist hingegen für jeden wichtig. Wir bieten Ihnen Sicherheit! Von Ihren professionellen Sicherheitsdiensten erhalten Sie maßgeschneiderte Konzepte, die Sie, Ihr Objekt oder Projekt langfristig schützen.</p>
  </div>
  <div class="box" style="left:28px;top:133px;width:207px;height:88px;padding:14px 12px;font-size:16px;line-height:1.15"><span class="light">DIE</span> <span class="bold">KWT NORD GMBH</span><br><span class="light">IHR PROFESSIONELLER</span><br><span class="bold">SICHERHEITSDIENST</span></div>
  <div class="col" style="left:28px;top:232px;width:207px;height:440px">
    <h4>Sicherheit für Deutschland und darüber hinaus</h4>
    <p>Die KWT Nord, der professionelle Sicherheitsdienst mit Sitz in Berlin, gibt Ihnen zuverlässige Schutz. Als erfahrene Profis im Bereich des Sicherheitsmanagements bieten wir allen Interessenten einen umfassenden Service. Wir schützen Privatpersonen, sichern Gebäude und Firmen und sorgen dafür, dass Ihre Veranstaltung ohne Zwischenfälle abläuft. Zufriedene Kunden aus vielen verschiedenen Ländern vertrauen auf die KWT Nord – und das zu Recht, denn mit unseren bestens ausgebildeten Mitarbeitern sind wir bundesweit und international sofort zur Stelle, wenn es um das Thema Sicherheit geht.</p>
    <h4>Eine Frage des Vertrauens: Ihre KWT Nord</h4>
    <p>Die KWT Nord GmbH rund um die Uhr für Sie im Einsatz. Für uns ist Sicherheit Vertrauenssache: Wir bieten Ihnen dank unserer langjährigen Erfahrung einen Service, auf den Sie sich wirklich verlassen können. Das starke Team der KWT Nord ist kompetent, perfekt ausgebildet und behält zu jeder Zeit einen kühlen Kopf. Als Sicherheitsdienst erkennen wir Krisensituationen schnell, greifen rechtzeitig ein und lösen jedes Problem auf professionelle Art. Zudem arbeiten unsere Mitarbeiter mit modernstem technischen Equipment – keine Chance für Störenfriede, Diebe und Vandalen!</p>
  </div>
  <div class="col" style="left:246px;top:32px;width:216px;height:640px">
    <h4>Diskreter Schutz in vielen Bereichen</h4>
    <p>Die KWT Nord ist als Sicherheitsdienst in vielen Bereichen tätig. Sie benötigen einen professionellen Personenschutz? Dann begleitet Sie unser diskretes Team auf Schritt und Tritt auf Wunsch natürlich auch mit entsprechender Bewaffnung. Sie haben mit Dieben oder Vandalen zu kämpfen? Kein Problem: Die KWT Nord sorgt in öffentlichen Einrichtungen, im Einzelhandel in Firmengebäuden, Hotels und auf Baustellen für Gebäudeschutz und Objektbewachung. An unseren kompetenten Wachmännern kommt keine verdächtige Person vorbei – mit Sicherheit! Große Events wie Messen, Konzerte oder Firmenfeiern sind durch den KWT-Veranstaltungsschutz natürlich ebenso zuverlässig geschützt.</p>
    <h4>Der flexible und professionelle Sicherheitsdienst</h4>
    <p>Aufgrund unserer dynamischen Organisationsstruktur können wir als Sicherheitsdienst besonders flexibel auf die Bedürfnisse unserer Kunden reagieren. Wir analysieren den spezifischen Bedarf an Sicherheitspersonal genau und entwickeln gemeinsam mit Ihnen das passende Sicherheitskonzept. Von Ihrer Sicherheitsfirma KWT Nord erhalten Sie eine individuelle Lösung, die Ihnen genau den Schutz bietet, den Sie brauchen. Zudem sind wir in vielen weiteren Bereichen für Sie im Einsatz, in denen hochzuverlässige und kompetente Teams gefragt sind. So unterstützen wir Sie nicht nur im Personen- und Objektschutz, sondern sind auch als Fahrunternehmen, Detektei International für Sie tätig.</p>
    <h4>Auf der sicheren Seite mit der KWT Nord</h4>
    <p>KWT Nord, Ihr Sicherheitsdienst für Deutschland und darüber hinaus, bietet Ihnen umfassenden und individuellen Service. Kommen Sie auf die sichere Seite und machen Sie sich selbst ein Bild von unseren Leistungen. Gerne beraten wir Sie unverbindlich über Ihre Möglichkeiten. Vereinbaren Sie Ihren persönlichen Beratungstermin einfach per Kontaktformular oder rufen Sie uns gebührenfrei unter 0800 555 0199 an. Als Partner in Sachen Sicherheit sind wir für Sie da!</p>
  </div>
</section>

<!-- Spread 2: Personenschutz / High Risk -->
<section class="page" style="left:110px;top:1582px;width:489px;height:685px">
  <div class="photo" role="img" aria-label="Erwachsener geht mit Kind an der Hand über ein Feld im Abendlicht" style="left:0;top:0;width:270px;height:272px;background:linear-gradient(160deg,#7d93b8 0%,#a48c6a 55%,#5b5038 100%)"></div>
  <div class="box" style="left:141px;top:17px;width:164px;height:71px;padding:8px 12px;text-align:right;font-size:27px;line-height:1"><span class="light">PERSONEN</span><br><span class="bold">SCHUTZ</span></div>
  <div class="col" style="left:28px;top:282px;width:208px;height:390px">
    <h4>KWT Nord – der professionelle Personenschutz</h4>
    <p>Die KWT Nord GmbH ist Ihr erfahrener Experte im Bereich Personenschutz und Begleitschutz. Für uns hat Ihre persönliche Sicherheit den höchsten Stellenwert. Ganz gleich, ob Sie eine Person des öffentlichen Lebens sind oder aufgrund Ihrer Lebensumstände bestimmten Bedrohungen ausgesetzt sind. Das professionelle Team der KWT Nord schützt Sie in allen Lebenslagen zuverlässig.</p>
    <h4>Endlich aufatmen: Wir garantieren Ihnen Sicherheit</h4>
    <p>Bei der KWT Nord arbeiten nur ausgewählte Mitarbeiter im Bereich Personenschutz und Begleitung welche Sie umfassend vor Gefahren schützen. Unser Team garantiert Ihnen aufgrund hervorragender Eignung und meist behördlicher Ausbildung bei der Polizei oder anderen staatlichen Sicherheitsstellen optimalen Schutz. Selbst extreme Gefährdungslagen sind für unsere auf Wunsch bewaffneten Leibwächter kein Problem. Ihr Personenschutz oder Begleitschutz behält in jeder Situation einen kühlen Kopf und bringt Sie unversehrt und sicher an Ihr Ziel.</p>
    <h4>Profitieren Sie von unserer umfassenden Erfahrung</h4>
    <p>Im Bereich Personenschutz agieren wir bundesweit und international. Hierbei können Sie sich auf den Service eines privaten Sicherheitsdienstes vollends verlassen. Bei uns buchen Sie nicht nur zuverlässige Leibwächter, sondern profitieren ebenso von unserer langjährigen Erfahrung. Dank unzähliger, erfolgreicher Praxiseinsätze im Bereich Personenschutz sind wir Ihr Experte, wenn es um das Thema Sicherheit geht. Deswegen vertrauen hochrangige Kunden aus Deutschland, aber auch aus dem internationalen Raum auf den zuverlässigen Service der KWT Nord.</p>
  </div>
  <div class="col" style="left:280px;top:97px;width:180px;height:575px">
    <h4>Sie werden individuell beraten und professionell betreut</h4>
    <p>Bei uns erhalten Sie keine x-beliebige Lösung. Denn zuverlässiger Personenschutz sollte immer genau auf die individuellen Anforderungen und Umstände der zu schützenden Person abgestimmt sein. Wir machen uns deshalb ein genaues Bild von Ihrer Situation und beraten Sie umfassend. So entwickeln wir ein einzigartiges und exakt auf Sie zugeschnittenes Sicherheitskonzept, das Ihnen genau den Schutz bietet, den Sie in Ihrer Lage benötigen. Auf dieser Grundlage stellen wir ein perfekt auf Ihren Anwendungsfall abgestimmtes Personenschutzteam zusammen.</p>
    <h4>Auf allerhöchstem Niveau: Personenschutz buchen bei der KWT Nord</h4>
    <p>Bei den Schutzkonzepten von KWT Nord steht die Prävention von Gefahren im Vordergrund. Wir verzichten auf aufgeblasenes Gehabe und setzen stattdessen auf Professionalität und Diskretion. Unsere Schützer sind darauf trainiert, in jeder Situation hochkonzentriert zu arbeiten. So haben wir zu jeder Zeit Ihre Person und Ihr Wohlbefinden im Blick und wahren jede Bedrohung zuverlässig, ab. Natürlich gehen wir mit absoluter Diskretion vor und lassen Ihnen den persönlichen Freiraum. Unser Personenschutz wird Sie im Alltag so wenig wie möglich einschränken.</p>
    <h4>Die Nummer 1 im Bereich Personenschutz und Begleitschutz</h4>
    <p>Die KWT Nord GmbH ist für Sie in Deutschland und darüber hinaus im Einsatz. Nutzen Sie Ihre Chance und buchen Sie unseren umfassenden und individuellen Service. Sie genießen fortan exzellenten Personenschutz oder Begleitschutz auf allerhöchstem Niveau. Natürlich bieten wir allen Interessenten die Möglichkeit, sich selbst ein Bild von unseren Leistungen zu machen. Vereinbaren Sie jetzt unverbindlich Ihren persönlichen Beratungstermin per Kontaktformular oder rufen Sie gebührenfrei unter der Telefonnummer 0800 555 0199 an. Ihr Sicherheitspartner ist für Sie da.</p>
  </div>
</section>
<section class="page" style="left:599px;top:1582px;width:489px;height:685px">
  <div class="photo" role="img" aria-label="Kletterer an einer steilen Felswand unter blauem Himmel" style="left:249px;top:0;width:240px;height:685px;background:linear-gradient(180deg,#6a8cc4 0%,#3f63a2 45%,#2c4478 100%)"></div>
  <div class="headline" style="left:28px;top:27px;font-size:17px;width:220px"><b>Ihr Sicherheits-<br>unternehmen</b> <span>für</span><br><b>High Risk</b> <span>Security</span><br><b>und maritime</b><br><span>Sicherheit</span></div>
  <div class="col" style="left:28px;top:130px;width:208px;height:540px">
    <p>Die KWT Nord GmbH ist Ihr Partner im Bereich High Risk Security und maritime Sicherheit. Wir stehen Ihnen mit Erfahrung und einem professionellen und flexiblen Service zur Seite selbst in hoch gefährdeten Gebieten bieten wir Ihnen zuverlässigen Schutz auf höchstem Niveau.</p>
    <h4>Ihr High Risk Spezialist</h4>
    <p>Bei der KWT Nord bekommen Sie umfangreiche Sicherheitsdienstleistungen für Risiko- und Krisengebiete. Wir arbeiten erfolgreich als High Risk Sicherheitsunternehmen international in den Bereichen bewaffneter Personen und Objektschutz und bieten internationale Transport Begleitungen im Maritimen Bereich. Auf dem Landweg und in der Luft. Auf das HR-Team der KWT Nord ist selbst in den höchsten Gefährdungslagen Verlass.</p>
    <h4>Das Sicherheitsunternehmen für Risiko und Krisengebiete</h4>
    <p>Die KWT Nord setzt im HR Bereich ausschließlich ausgewählte Mitarbeiter ein. Unser HR-Team besteht aus entsprechend geschulten Mitarbeitern mit Militärische Ausbildung, welche bereits ausführliche Praxiserfahrung im HR-Bereich aufweisen. Wir ergänzen unsere HR-Teams zudem immer mit weiteren, lokalen Mitarbeitern aus unserem internationalen Netzwerk.</p>
    <h4>Im Beratungstermin erfahren Sie mehr</h4>
    <p>Wir gehen Neuaufträge stets professionell und fokussiert an und analysieren die Anforderungen genau: In unserem Beratungsgespräch besprechen wir alle wichtigen Details mit Ihnen und planen die nötigen Einsatzkräfte und Ressourcen. Dank der umfassenden Vorausplanung erhalten Sie bei der KWT Nord einen individuelles und zuverlässiges Schutzkonzept.</p>
    <h4>Sicherheitsunternehmen für High Risk Security: Buchen Sie jetzt Ihren Beratungstermin!</h4>
    <p>Die KWT Nord GmbH ist rund um die Uhr für Sie im Einsatz. Wir schützen Ihre Person, weitere Begleiter oder ganze Objekte in Risiko- und Krisengebieten. Vertrauen Sie auf Ihren professionellen HR-Sicherheitsdienstleister.</p>
  </div>
  <div class="box" style="left:191px;top:574px;width:298px;height:98px;padding:18px 0 0 30px;font-size:31px;line-height:1"><span class="light">HIGH RISK</span><br><span class="bold">SECURITY</span></div>
</section>

<!-- Spread 3: Fahrerservice / Objektschutz -->
<section class="page" style="left:110px;top:2283px;width:489px;height:688px">
  <div class="col" style="left:28px;top:23px;width:208px;height:380px">
    <h4>KWT Nord – der zuverlässige Fahrdienst</h4>
    <p>Fahrservice gesucht? Dann melden Sie sich bei der KWT Nord GmbH. Wir bieten Ihnen hervorragende Fahrer und einen zuverlässigen Fahrservice – und das nicht nur im gesamten Bundesgebiet. Unseren Fahrdienst können Sie weit über die Grenzen Deutschlands in Anspruch nehmen. Wir bringen Sie dank unseres hervorragenden Fahrerservices zu jeder Zeit und mit Sicherheit an Ihr Wunschziel!</p>
    <h4>Top in Form: Die Fahrer der KWT Nord GmbH</h4>
    <p>Wenn Sie den Fahrdienst von KWT Nord in Anspruch nehmen, hat Ihre Sicherheit im Straßenverkehr oberste Priorität. Wir bieten Ihnen daher ausschließlich kompetente Fahrer, die mit ihrer langjährigen Fahrpraxis überzeugen. Unsere qualifizierten Mitarbeiter beweisen in allen Situationen Ruhe und fahrerisches Können. Sie sind außerdem angewiesen, stets defensiv und der Verkehrslage entsprechend zu agieren. Weiterhin können wir Ihnen dank unseres Netzwerks immer ortskundige Fahrer bereitstellen, die sich in der jeweiligen Region bestens auskennen.</p>
    <h4>Unsere ausgesuchten Mitarbeiter werden regelmäßig geprüft</h4>
    <p>Wir wissen: Vertrauen ist gut, Kontrolle ist jedoch besser. Deshalb führen wir in konstanten Intervallen Fahrtrainings. Die KWT Nord stellt mit diesen Maßnahmen sicher, dass stets die optimale Qualität des Fahrservices gewährleistet ist. Sie können sich also gewiss sein, dass Sie wohlbehalten und ohne Zwischenfälle am Zielort eintreffen.</p>
  </div>
  <div class="col" style="left:247px;top:23px;width:210px;height:380px">
    <h4>KWT Nord: Ihr High Security-Fahrdienst</h4>
    <p>Als Security-Experte kümmern wir uns für Sie zuverlässig um alle Transporte, an die besondere hohe Sicherheitsanforderungen gestellt werden. Mit umfassender Erfahrung im Bereich Sicherheit und Personenschutz bieten wir Ihnen selbstverständlich auch passende Fahrer in diesen Bereichen an. Unsere Mitarbeiter im Fahrdienst wissen nicht nur, was im Ernstfall zu tun ist, sondern erkennen bereits im Vorfeld potenzielle Risikofaktoren. Wir garantieren Ihnen: Geld- und Wertgegenstände bringen wir genauso wohlbehalten ans Ziel, wie Personen in Gefährdungslagen.</p>
    <h4>Professionell – und natürlich freundlich und höflich</h4>
    <p>Bei der KWT Nord buchen Sie den umfassenden Fahrservice. Wir bieten Ihnen nicht nur professionelle Fahrer, die Ihre Wünsche schnell und zuverlässig erledigen. Unsere Mitarbeiter sind zudem diskret, höflich und freundlich. Sie wollen den Fahrdienst persönlich nutzen oder Ihren Gästen zur Verfügung stellen? Dann können Sie sich auf freundliche Fahrer mit exzellenten Umgangsformen freuen.</p>
    <h4>Buchen Sie jetzt Ihren Fahrdienst!</h4>
    <p>Wann immer Sie es wünschen, steht Ihnen die KWT Nord GmbH als professioneller Fahrdienst zur Verfügung. Wir bringen Personen und Frachtgut bundes- und europaweit sicher und pünktlich an den gewünschten Bestimmungsort.</p>
  </div>
  <div class="photo" role="img" aria-label="Chauffeur im Anzug am Steuer eines Wagens" style="left:0;top:412px;width:358px;height:276px;background:linear-gradient(120deg,#c9ced6 0%,#8a95a6 50%,#3b4456 100%)"></div>
  <div class="headline" style="left:372px;top:422px;font-size:19px;line-height:1.1;color:var(--navy)"><b>Vertrauen</b><br><span>ist gut,</span><br><b>Kontrolle</b><br><span>ist jedoch</span><br><b>besser.</b></div>
  <div class="box" style="left:252px;top:553px;width:154px;height:119px;padding:22px 0 0 18px;font-size:29px;line-height:1"><span class="light">FAHRER</span><br><span class="bold">SERVICE</span></div>
</section>
<section class="page" style="left:599px;top:2283px;width:489px;height:688px">
  <div class="photo" role="img" aria-label="Weiße Überwachungskamera an einer Wand" style="left:161px;top:0;width:328px;height:323px;background:linear-gradient(150deg,#5a7cb8 0%,#9fb2d0 50%,#3c5a95 100%)"></div>
  <div class="box" style="left:161px;top:32px;width:132px;height:97px;padding:10px 0 0 10px;font-size:28px;line-height:1"><span class="light">OBJEKT</span><br><span class="bold">SCHUTZ</span></div>
  <div class="headline" style="left:28px;top:67px;font-size:16px;line-height:1.1"><b>KWT Nord</b> <span>– der</span><br><span>zuverlässige</span><br><b>Objektschutz</b></div>
  <div class="col" style="left:28px;top:168px;width:200px;height:505px">
    <p>Der Objektschutz spielt für viele Immobilien im privaten, gewerblichen und öffentlichen Bereich eine große Rolle. Unsere geschulten Sicherheitsfachkräfte gewährleisten, dass der tägliche Betrieb im Gebäude ordnungsgemäß abläuft und keine unberechtigten Personen oder anderen ungebetenen Gäste Zutritt erhalten. Der erfahrene Ansprechpartner für diese Aufgabe ist die KWT Nord. Wir gewährleisten Sicherheit für Ihre Immobilie und stehen Ihnen als zuverlässiger und professioneller Dienstleister zur Seite.</p>
    <h4>Sicherheit für Gebäude von der KWT Nord</h4>
    <p>Die KWT Nord sichert Privatimmobilien, Gewerbegebäude und öffentliche Einrichtungen mit professionellen Objektschutzmaßnahmen. Wir übernehmen die tägliche und nächtliche Bestreifung des Geländes und der Innenflächen und führen auf Wunsch Personal- und Zutrittskontrollen sowie Observationsmaßnahmen mittels Videoüberwachungsanlagen durch. Neben der Bewachung der Zugänge und Innenflächen sichern wir ebenso das gesamte befriedetes Besitztum ab. Dabei stellen wir unsere Objektschutz-Maßnahmen ab. Dank unserer Arbeit schützen wir Sie, Ihre Mitarbeiter und Besucher und sorgen für Ordnung plus Sicherheit. Selbst im Ernstfall behalten die hervorragend ausgebildeten Mitarbeiter von KWT Nord einen kühlen Kopf und lösen Problemsituation und Konflikte schnell.</p>
    <h4>Service von der KWT Nord für Unternehmen und Institutionen aller Art</h4>
    <p>Viele zufriedene Kunden aus den Bereichen Einzelhandel, Industrie, sowie öffentliche Einrichtungen und Behörden vertrauen auf die KWT Nord. Mit unserem Objektschutz unterstützen wir Bundeswehr, verschiedene Unternehmen und Institutionen mit hohem Sicherheitsbedarf. Zudem betreuen wir Messen, Krankenhäuser, Erstaufnahmeeinrichtungen und Asylunterkünfte. Für Bauherren stehen zudem unsere Profis zur Baustellenbewachung bereit.</p>
  </div>
  <div class="col" style="left:246px;top:333px;width:216px;height:340px">
    <h4>Der umfassende Service von der KWT Nord</h4>
    <p>Der KWT Nord geht den Objektschutz individuell und auf die Bedürfnisse des Kunden zugeschnitten an. So machen wir uns stets ein umfassendes Bild vor Ort und stellen für Sie ein lokales und ortkundiges Team zusammen, das perfekt auf den spezifischen Einsatzweck abgestimmt ist. Wir haben immer ein offenes Ohr für Ihre Wünsche und unterstützen Sie gerne auch bei der sicherheitstechnischen Ausstattung. Die KWT Nord übernimmt bei Bedarf die Technische Nachrüstung des Gebäudes.</p>
    <h4>Buchen Sie jetzt den Objektschutz von der KWT Nord!</h4>
    <p>Auf die Gebäudesicherheit von der KWT Nord können Sie sich verlassen. Wir stellen die passenden Spezialisten bereit und bringen Ihre Immobilie sicherheitstechnisch auf den neuesten Stand. Hervorzuheben ist nicht zuletzt unsere transparente Arbeitsweise: Auf Kundenwunsch senden wir Ihnen die Protokolle der Wächter zu und weisen so die Bestreifungszeiten. Schon während der Planungsphase Ihres Gebäudes können Sie die KWT Nord miteinbeziehen, um so von Anfang an ein umfassendes Sicherheitskonzept zu erarbeiten. Natürlich steht Ihnen ebenso die Buchung weiterer Leistungen wie etwa unserer Sicherheitstechnik offen.</p>
  </div>
</section>

<!-- Spread 4: Brandsicherheit / Zitat -->
<section class="page" style="left:110px;top:2985px;width:489px;height:685px">
  <div class="col" style="left:28px;top:20px;width:208px;height:360px">
    <h4>KWT Nord – Brandsicherheitswache</h4>
    <p>Sie möchten sich zuverlässig vor Bränden schützen? Dann vertrauen Sie auf die KWT Nord. Unsere zertifizierte Brandsicherheitswache unterstützt Sie gerne im Bereich der Brandprävention. Wir schützen Ihre Baustelle oder Ihre Veranstaltung vor Feuer aller Art.</p>
    <h4>Die zuverlässige Brandwache für Veranstaltungen und Baustellen</h4>
    <p>Die Brandsicherheitswache der KWT Nord ist auf Brandschutzmaßnahmen für Baustellen und Veranstaltungen spezialisiert. Wir beseitigen alle Brandquellen und stellen sicher, dass Feuer gar nicht erst entstehen kann. Sollte es auf Ihrem Baugrund oder Ihrem Event dennoch zum Notfall kommen, behalten unsere Mitarbeiter einen kühlen Kopf und den Überblick. Wir wissen, was im Ernstfall zu tun ist, und leiten schnell und zuverlässig Gegenmaßnahmen ein. Zudem können Sie sich auch dann auf uns verlassen, wenn Ihre Brandmeldeanlage (BMA) oder Ihre Sprinkleranlage einmal ausfallen sollten.</p>
    <h4>Das professionelle Brandschutzkonzept der KWT Nord</h4>
    <p>Eine Brandsicherheitswache ist bei allen größeren Veranstaltungen nach der Versammlungsstättenverordnung in der Regel vorgeschrieben. Dies trifft zumeist auf Veranstaltungsflächen ab 200 Quadratmetern zu. Aber auch kleinere Events sollten über den passenden Brandschutz verfügen. So stellen Sie als Veranstalter sicher, dass keine Personen noch Sachgegenstände zu Schaden kommen. Wir</p>
  </div>
  <div class="col" style="left:250px;top:20px;width:210px;height:360px">
    <p>von der KWT Nord bestimmen Ihren Bedarf genau. Wir ermitteln durch eine Gefährdungsanalyse, welche Brandpräventionsmaßnahmen für Sie infrage kommen. Auf dieser Grundlage stellen wir das passende Team aus Brandschutzspezialisten zusammen. Sie können sich auf unsere hervorragend ausgebildeten Mitarbeiter absolut verlassen und sich weiterhin um die Planung Ihrer Veranstaltung oder den Betrieb Ihrer Baustelle kümmern.</p>
    <h4>KWT Nord: Keine Chance für Brände</h4>
    <p>Die Brandsicherheitswache der KWT Nord setzt alle Regeln und Auflagen zur Brandprävention auf Baustellen und Veranstaltungen um. Dazu gehört unter anderem die Personalkontrolle vor Ort. Alle Mitarbeiter im Betrieb sind eingehalten. Wir sorgen außerdem dafür, dass keine Gegenstände wie Feuerwerkskörper oder Haarsprays vor Ort gelangen, die ein Risiko darstellen. Außerdem kontrollieren wir die Stelle, sobald das kleinste Feuerchen entsteht. Mittels Kleinlöschgeräten sowie der Brandwacheausrüstung erstickt wir das Feuer im Keim. Im Falle einer größeren Brandgefahr alarmiert unser Team natürlich umgehend die Feuerwehr und hilft bei der Evakuierung von Besuchern und Personal.</p>
    <h4>Drei gute Gründe für unsere Brandsicherheitswache</h4>
    <p>› Langjährige Erfahrung als Sicherheitsspezialist im Bereich Brandprävention<br>› Zuverlässiges und individuelles Brandschutzkonzept aus einer Hand<br>› Bestmöglicher Schutz durch professionell ausgebildete Mitarbeiter</p>
  </div>
  <div class="col" style="left:330px;top:415px;width:130px;height:165px">
    <p>Lassen Sie sich jetzt unverbindlich beraten! Überzeugen Sie sich jetzt selbst von unserem Service. Vereinbaren Sie noch heute Ihren Erstberatungstermin für unsere Brandsicherheitswache. Wir besprechen potenzielle Maßnahmen und geben Ihnen einen Überblick über die nötigen Einsatzkräfte.</p>
  </div>
  <div class="photo" role="img" aria-label="Rote Feuerlöscher und Feuerwehrhelm" style="left:0;top:380px;width:323px;height:305px;background:linear-gradient(135deg,#b54848 0%,#7a2c2c 55%,#3a2f3a 100%)"></div>
  <div class="box" style="left:0;top:496px;width:420px;height:124px;padding:50px 0 0 128px;font-size:30px;line-height:1"><span class="light">BRAND</span><span class="bold">SICHERHEIT</span></div>
</section>
<section class="page" style="left:599px;top:2985px;width:489px;height:685px">
  <div class="photo" role="img" aria-label="Zwei Personen mit erhobenen Armen auf einer Klippe über weiter Landschaft bei Sonnenuntergang" style="left:0;top:0;width:489px;height:685px;background:linear-gradient(180deg,#5f78a6 0%,#8f9bb0 35%,#c3a873 55%,#5d6a48 75%,#2e3a2c 100%)"></div>
  <div class="box" style="left:28px;top:355px;width:341px;height:132px;padding:22px 18px 0 14px;text-align:right">
    <div style="font-size:30px;line-height:1.05"><span class="light">„OHNE</span> <span class="bold">SICHERHEIT</span> <span class="light">IST</span><br><span class="light">KEINE</span> <span class="bold">FREIHEIT.</span> <span class="bold">„</span></div>
    <div style="font-family:'Roboto',sans-serif;font-size:8.5px;margin-top:10px">Friedrich Lenhart</div>
  </div>
</section>

<!-- Back cover: Kontakt -->
<section class="page" style="left:353px;top:3688px;width:492px;height:687px">
  <div class="box" style="left:32px;top:23px;width:242px;height:600px;background:var(--blue)"></div>
  <div class="box" style="left:32px;top:23px;width:295px;height:109px;padding:42px 0 0 80px;font-size:32px;line-height:1;background:var(--blue-soft)"><span class="light">KON</span><span class="bold">TAKT</span></div>
  <div class="col contact" style="left:297px;top:180px;width:180px;height:460px;font-size:10px;line-height:1.3;text-align:left;color:var(--navy)">
    <p><b>Hauptniederlassung Berlin</b><br><i>KWT Sicherheitsgruppe<br>Havel GmbH</i></p>
    <p style="margin-top:8px">Lindenweg 14,<br>13591 Berlin<br>Tel: +49 (0) 30 555 01 20<br>Fax: +49 (0) 30 555 01 21<br>E-Mail: info@kwt-beispiel.de</p>
    <p style="margin-top:26px"><b>Abteilung Maritime Sicherheit</b><br><i>KWT Sicherheitsgruppe<br>Havel GmbH</i></p>
    <p style="margin-top:8px">Hafenstraße 8,<br>18055 Rostock<br>Tel: 0381 / 555 02 10<br>Fax: 0381 / 555 02 11<br>E-Mail: info@kwt-beispiel.de</p>
    <p style="margin-top:26px"><b>Abteilung Flughafensicherheit</b><br><i>KWT Sicherheitsgruppe<br>Havel GmbH</i></p>
    <p style="margin-top:8px">Feldallee 21,<br>12526 Berlin<br>Tel: 030 / 555 03 40<br>Fax: 030 / 555 03 41<br>E-Mail: info@kwt-beispiel.de</p>
  </div>
</section>

</body>
</html>
```